" empresa presta consultoria na área de gestão financeira e assistência técnica para propriedade/empresa rural. Possui em seu quadro engenheiros agrônomos e médicos veterinários, altamente capacitados. Atua fortemente na área de financiamento rural e gestão de projetos junto à instituições financeiras. "

```html
<!DOCTYPE html>
<html lang="pt-BR">
<head>
<meta charset="UTF-8">
<title>Agrivale — Papel timbrado</title>
<link href="https://fonts.googleapis.com/css2?family=Montserrat:wght@400;500;600&display=swap" rel="stylesheet">
<style>
  :root{
    --backdrop:#bcbdbf;
    --paper:#ffffff;
    --gold:#b99a6b;
    --gold-light:#d9c39a;
    --gold-dark:#9c7d4f;
    --watermark:#f1ece4;
    --navy:#1e2733;
    --ink:#3a3f47;
  }
  *{margin:0;padding:0;box-sizing:border-box}
  html,body{width:1200px;height:1200px;overflow:hidden}
  body{background:var(--backdrop);font-family:'Montserrat',sans-serif;position:relative}
  .letterhead{
    position:absolute;left:372px;top:271px;width:456px;height:658px;
    background:var(--paper);
  }
  .brand{
    position:absolute;top:24px;left:0;width:100%;
    display:flex;flex-direction:column;align-items:center;
  }
  .brand-dot{width:22px;height:22px;border-radius:50%;background:var(--gold);margin-bottom:6px}
  .brand-name{
    font-weight:600;font-size:15px;letter-spacing:4px;color:var(--gold);line-height:1;
  }
  .brand-tagline{
    margin-top:4px;font-size:5.5px;letter-spacing:1.6px;text-transform:uppercase;color:var(--gold);
  }
  .watermark{
    position:absolute;left:72px;top:156px;width:312px;height:312px;border-radius:50%;
    background:radial-gradient(circle at 50% 40%, #f4f0ea 0%, var(--watermark) 70%);
  }
  .contacts{
    position:absolute;left:0;width:100%;top:591px;
    display:flex;flex-direction:column;align-items:center;gap:6px;
    font-size:6.5px;color:var(--ink);
  }
  .contact-row{display:flex;gap:14px;align-items:center}
  .contact-item{display:flex;align-items:center;gap:4px;white-space:nowrap}
  .contact-item svg{width:9px;height:9px;flex:none}
  .rule-gold{
    position:absolute;left:0;width:100%;top:637px;height:4px;
    background:linear-gradient(90deg,var(--gold-dark),var(--gold-light) 50%,var(--gold-dark));
  }
  .rule-navy{position:absolute;left:0;width:100%;top:646px;height:12px;background:var(--navy)}
</style>
</head>
<body>
  <main class="letterhead">
    <header class="brand">
      <span class="brand-dot"></span>
      <span class="brand-name">AGRIVALE</span>
      <span class="brand-tagline">Consultoria e Gestão Rural</span>
    </header>

    <div class="watermark" role="img" aria-label="Símbolo da marca em marca-d'água: animal sobre campo em linhas curvas"></div>

    <footer class="contacts">
      <div class="contact-row">
        <span class="contact-item">
          <svg viewBox="0 0 10 10"><circle cx="5" cy="5" r="5" fill="#3a3f47"/><path d="M3.3 2.6l1 .9-.5.8a4 4 0 0 0 1.9 1.9l.8-.5.9 1-.7.8C4.6 7.3 2.7 5.4 2.6 3.3z" fill="#fff"/></svg>
          +55 11 4000-2100
        </span>
        <span class="contact-item">
          <svg viewBox="0 0 10 10"><circle cx="5" cy="5" r="5" fill="#3a3f47"/><rect x="2.5" y="3.2" width="5" height="3.6" fill="none" stroke="#fff" stroke-width=".7"/><path d="M2.5 3.2L5 5.2l2.5-2" fill="none" stroke="#fff" stroke-width=".7"/></svg>
          contato@agrivale.com.br
        </span>
        <span class="contact-item">
          <svg viewBox="0 0 10 10"><circle cx="5" cy="5" r="5" fill="#3a3f47"/><circle cx="5" cy="5" r="2.6" fill="none" stroke="#fff" stroke-width=".6"/><path d="M2.4 5h5.2M5 2.4c-1.2 1.5-1.2 3.7 0 5.2M5 2.4c1.2 1.5 1.2 3.7 0 5.2" fill="none" stroke="#fff" stroke-width=".5"/></svg>
          www.agrivale.com.br
        </span>
      </div>
      <div class="contact-row">
        <span class="contact-item">
          <svg viewBox="0 0 10 10"><circle cx="5" cy="5" r="5" fill="#3a3f47"/><path d="M5 2a2 2 0 0 1 2 2c0 1.5-2 3.8-2 3.8S3 5.5 3 4a2 2 0 0 1 2-2z" fill="#fff"/><circle cx="5" cy="4" r=".7" fill="#3a3f47"/></svg>
          Rua das Palmeiras, 120 - Centro - São Paulo - SP
        </span>
      </div>
    </footer>

    <div class="rule-gold"></div>
    <div class="rule-navy"></div>
  </main>
</body>
</html>
```